Flyer Design Project

I provide workshops for teachers, students and parents on organization - specifically laying out 3 goals, their accompanying activities and actions in 3 three hour sessions.

Please go to my website to see my brain logo. I need a flyer with the information typed below. The information may be changed and/or added to in way you see fit to better communicate the organizational intent.This is not for speech therapy clients, rather, it is for any and everyone who needs help writing out goals.

I would like the design of the flyer to reflect the concept of organization in a unique way.

http://brightvoicestudio-example.com/wp-content/uploads/2012/02/websitelogo2.jpg

ORGANIZATION

Write out your goals for the year.

How to organize your life in 3 easy steps.
Have fun organizing your life and plans.
Join a group of people dedicated to organizing all areas of life.
Complete your tasks in a fast, fun game format.
Walk away with your major goals broken down into their component parts and organize on a yearly calendar.
Three 3 hour days spent in making your life happier, less stressed and with realistic picture of what needs to be accomplished.
more effective in everything I do.
Being organized helps free our minds, enjoy relationships more, feel happier, and have greater meaning in life.

You will walk away with detailed plans for 2013.

COST: $600 for all three days.

WHO: Led by Marlene Tuvik, Cognitive Speech Therapist
WHERE: 4127 E Holm Ave
Pasco, WA 99301
509-555-0187

Requirements
Must have
• My logo from my website. A unique organized appearance.

```html
<!DOCTYPE html>
<html lang="en">
<head>
<meta charset="utf-8">
<title>Goals, Activities, Actions – Workshop Flyer</title>
<link href="https://fonts.googleapis.com/css2?family=Arimo:wght@400&family=Crimson+Pro:ital,wght@0,400;0,600;1,600;1,700&display=swap" rel="stylesheet">
<style>
  :root{
    --cream:#fbf7df;
    --cream-deep:#f2ecc4;
    --rule-orange:#e59a2b;
    --navy:#0c2a4a;
    --navy-mid:#123d63;
    --teal:#1d6b8e;
    --gold:#f4c21a;
    --ink:#222222;
    --white:#ffffff;
    --art-orange:#e8731f;
    --art-red:#c93a22;
    --art-blue:#2a7fc0;
    --photo-skin:#c9a98e;
    --photo-grey:#cfd3d6;
  }
  *{margin:0;padding:0;box-sizing:border-box}
  html,body{width:871px;height:1200px;overflow:hidden;background:var(--white)}
  body{font-family:"Crimson Pro",Georgia,serif;color:var(--ink)}
  .flyer{position:relative;width:871px;height:1200px;overflow:hidden;background:var(--white)}

  .masthead{position:absolute;left:0;top:0;width:871px;height:115px;
    background:linear-gradient(180deg,var(--cream),var(--cream-deep));
    border-bottom:4px solid var(--rule-orange)}
  .brand{position:absolute;left:22px;top:30px;display:flex;align-items:center;gap:14px}
  .brand-dot{width:54px;height:54px;border-radius:50%;background:var(--navy-mid)}
  .brand-name{font-weight:600;font-size:31px;color:var(--navy-mid);line-height:1}
  .leader{position:absolute;right:26px;top:16px;text-align:right;font-size:21px;line-height:28px;color:var(--ink)}

  .hero{position:absolute;left:0;top:115px;width:871px;height:345px}
  .hero svg{position:absolute;left:0;top:0;display:block}
  .idea-art{position:absolute;left:14px;top:18px;width:370px;height:276px;border-radius:6px;
    background:linear-gradient(135deg,var(--gold) 0%,var(--art-orange) 40%,var(--art-red) 55%,var(--art-orange) 70%,var(--art-blue) 100%);
    opacity:.9}
  .pillar{position:absolute;right:40px;font-style:italic;font-weight:600;font-size:52px;color:var(--white);letter-spacing:1px;line-height:1}
  .pillar.goals{top:50px}
  .pillar.activities{top:116px}
  .pillar.actions{top:180px}

  .team-photo{position:absolute;left:0;top:462px;width:400px;height:542px;
    background:radial-gradient(ellipse at 50% 45%,var(--photo-skin) 0%,var(--photo-grey) 55%,var(--white) 100%)}

  .benefits{position:absolute;left:429px;top:472px;width:412px}
  .benefits h1{font-style:italic;font-weight:700;font-size:33px;line-height:37px;color:var(--teal);margin-bottom:26px}
  .benefits ul{list-style:none}
  .benefits li{position:relative;padding-left:27px;font-family:Arimo,Arial,sans-serif;font-size:16.5px;line-height:20px;margin-bottom:18px;text-align:justify}
  .benefits li::before{content:"";position:absolute;left:2px;top:6px;width:9px;height:9px;border-radius:50%;background:var(--gold)}

  .takeaway{position:absolute;left:44px;top:1032px;font-style:italic;font-weight:700;font-size:30px;line-height:38px;color:var(--teal)}
  .cost{position:absolute;left:429px;top:1038px;font-style:italic;font-weight:700;font-size:22px;color:var(--ink)}

  .footer{position:absolute;left:0;bottom:0;width:871px;height:120px}
  .footer svg{position:absolute;left:0;top:0}
  .address{position:absolute;left:40px;bottom:18px;font-size:19px;color:var(--white)}
  .call{position:absolute;right:26px;bottom:16px;text-align:right;color:var(--white);line-height:1}
  .call-label{font-size:37px;display:block;margin-bottom:8px}
  .call-number{font-size:41px;display:block}
</style>
</head>
<body>
<main class="flyer">

  <header class="masthead">
    <div class="brand">
      <span class="brand-dot"></span>
      <span class="brand-name">Bright Voice Learning Studio</span>
    </div>
    <div class="leader">
      <div>ProgramLed by</div>
      <div>Marlene Tuvik</div>
      <div>Cognitive Speech Therapist</div>
    </div>
  </header>

  <section class="hero">
    <svg width="871" height="345" viewBox="0 0 871 345" aria-hidden="true">
      <defs>
        <linearGradient id="heroBand" x1="0" y1="0" x2="1" y2="0">
          <stop offset="0" stop-color="#0a2342"/>
          <stop offset=".6" stop-color="#14406a"/>
          <stop offset="1" stop-color="#1a5684"/>
        </linearGradient>
        <linearGradient id="heroEdge" x1="0" y1="0" x2="1" y2="0">
          <stop offset="0" stop-color="#9aa4ad"/>
          <stop offset="1" stop-color="#e9ecee"/>
        </linearGradient>
      </defs>
      <polygon points="0,0 871,0 871,262 742,262 718,332 0,332" fill="url(#heroBand)"/>
      <polygon points="718,332 742,262 871,262 871,280 758,280 734,337 0,337 0,332" fill="url(#heroEdge)"/>
    </svg>
    <div class="idea-art" role="img" aria-label="Colourful illustration of interlocking gears forming a thinking head"></div>
    <svg width="871" height="345" viewBox="0 0 871 345" aria-hidden="true">
      <g stroke="#ffffff" stroke-width="3" fill="none">
        <polyline points="199,54 225,78 652,78"/>
        <line x1="239" y1="143" x2="548" y2="143"/>
        <polyline points="194,219 222,207 602,207"/>
      </g>
      <g fill="#f4c21a">
        <polygon points="650,70 666,78 650,86"/>
        <polygon points="546,135 562,143 546,151"/>
        <polygon points="600,199 616,207 600,215"/>
      </g>
      <g fill="#ffffff">
        <circle cx="199" cy="54" r="12"/>
        <circle cx="239" cy="143" r="12"/>
        <circle cx="194" cy="219" r="12"/>
      </g>
    </svg>
    <div class="pillar goals">GOALS</div>
    <div class="pillar activities">ACTIVITIES</div>
    <div class="pillar actions">ACTIONS</div>
  </section>

  <div class="team-photo" role="img" aria-label="Photo of a cheerful group of adults giving thumbs up"></div>

  <section class="benefits">
    <h1>WRITE OUT YOUR<br>GOALS FOR THE YEAR</h1>
    <ul>
      <li>Have fun organizing your life and plans in 3 Easy Steps</li>
      <li>Join a group of people dedicated to organizing all areas of life.</li>
      <li>Complete your tasks in a fast, fun game format.</li>
      <li>Walk away with your major goals broken-down into their component parts and organize on a yearly calendar.</li>
      <li>Three days &amp; three hours a day spent in making your life happier, less stressed .</li>
      <li>Be more effective in everything you do.</li>
      <li>Being organized helps free our minds, enjoy relationships more, feel happier, and have greater meaning in your life.</li>
    </ul>
  </section>

  <p class="takeaway">You will walk away with<br>detailed plans for 2013.</p>
  <p class="cost">COST: $600 for all three days.</p>

  <footer class="footer">
    <svg width="871" height="120" viewBox="0 0 871 120" aria-hidden="true">
      <defs>
        <linearGradient id="footBand" x1="0" y1="0" x2="1" y2="0">
          <stop offset="0" stop-color="#3aa3c9"/>
          <stop offset=".45" stop-color="#1d6b8e"/>
          <stop offset="1" stop-color="#0c3a5e"/>
        </linearGradient>
      </defs>
      <polygon points="385,30 430,0 871,0 871,120 0,120 0,58 370,58" fill="url(#footBand)"/>
      <polygon points="0,52 366,52 381,24 426,-6 432,0 386,30 370,58 0,58" fill="#c7ced3"/>
    </svg>
    <div class="address">4127 E Holm Ave Pasco, WA 99301</div>
    <div class="call">
      <span class="call-label">Call Us</span>
      <span class="call-number">509-555-0187</span>
    </div>
  </footer>

</main>
</body>
</html>
```